Dewleaf Botanica. Home based organic skin care manufacturer

We need top notch user friendly and interactive web6/mobile site that will cater to online e commerce, retail of our varieties of products and real time communication with online buyers.

```html
<!DOCTYPE html>
<html lang="en">
<head>
<meta charset="utf-8">
<title>Dewleaf Botanica — Home Based Organic Skin Care</title>
<link href="https://fonts.googleapis.com/css2?family=Montserrat:wght@400;500;600;700&display=swap" rel="stylesheet">
<style>
:root{
  --rose:#d0a29b;
  --rose-dark:#b98880;
  --blush:#f6eeec;
  --blush-2:#f3e7e4;
  --cocoa:#4a3734;
  --cocoa-deep:#3b2926;
  --ink:#2f2a29;
  --text:#4d4645;
  --muted:#9a8f8d;
  --white:#ffffff;
}
*{margin:0;padding:0;box-sizing:border-box}
html,body{width:1200px;height:4237px;overflow:hidden}
body{font-family:'Montserrat',sans-serif;color:var(--text);background:var(--white);position:relative}
.abs{position:absolute}
.btn{position:absolute;background:var(--rose);color:var(--white);font-size:11px;letter-spacing:2px;text-transform:uppercase;display:flex;align-items:center;justify-content:center}
h2.section-title{position:absolute;left:0;width:1200px;text-align:center;font-size:22px;font-weight:600;color:var(--ink);letter-spacing:1px;text-transform:uppercase}

/* top bar */
.promo-bar{left:0;top:0;width:1200px;height:33px;background:var(--rose);color:var(--white);font-size:11px;display:flex;align-items:center;justify-content:center}

/* hero */
.hero{left:0;top:33px;width:1200px;height:588px;background:linear-gradient(180deg,#f3ebe9 0%,#f7f0ef 60%,#f5eceb 100%)}
.brand{display:flex;align-items:center;gap:8px;font-size:13px;letter-spacing:2px;text-transform:uppercase;color:var(--ink);font-weight:500}
.brand-dot{width:12px;height:12px;border-radius:50%;background:var(--rose)}
.header-brand{left:30px;top:25px}
.main-nav{left:477px;top:32px;display:flex;gap:0;font-size:12px;letter-spacing:1.2px;color:var(--ink)}
.main-nav span{position:absolute;white-space:nowrap}
.nav-icons{left:1090px;top:30px;display:flex;gap:14px}
.hero-title{left:197px;top:215px;font-size:39px;line-height:44px;font-weight:700;color:var(--cocoa);text-transform:uppercase}
.hero-sub{left:197px;top:316px;font-size:16px;line-height:27px;color:var(--ink);width:380px}
.signup{left:199px;top:393px;width:413px;height:39px;border:1px solid #d9cbc8;border-radius:20px;background:var(--white)}
.signup-field{position:absolute;left:22px;top:12px;font-size:11px;color:#b5aaa8}
.signup-btn{position:absolute;right:-1px;top:-1px;width:108px;height:39px;border-radius:20px;background:var(--rose);color:var(--white);font-size:11px;display:flex;align-items:center;justify-content:center}
.hero-photo{left:650px;top:131px;width:468px;height:457px;border-radius:230px 230px 0 0;background:radial-gradient(ellipse at 50% 45%,#efd6cb 0%,#e9cdc1 45%,#f3e8e4 100%)}

/* about */
.about-photo{left:268px;top:671px;width:261px;height:320px;border-radius:130px 130px 40px 130px;background:linear-gradient(160deg,#f1e3dc,#dcc0b3 60%,#eadcd6)}
.about-inset{left:224px;top:880px;width:110px;height:110px;border-radius:50%;border:5px solid var(--white);background:radial-gradient(circle,#efe6d8,#c9b59b);box-shadow:0 4px 10px rgba(0,0,0,.15)}
.about-title{left:613px;top:725px;font-size:27px;font-weight:600;color:var(--ink);letter-spacing:1px}
.about-copy{left:613px;top:773px;width:380px;font-size:11.5px;line-height:19.5px;color:var(--text)}
.about-copy p+p{margin-top:7px}

/* offers */
.offers{left:0;top:1072px;width:1200px;height:408px;background:var(--cocoa)}
.offers h2.section-title{color:var(--white);top:40px}
.offer{position:absolute;top:91px;width:240px;margin-left:-120px;text-align:center}
.offer-circle{width:210px;height:210px;border-radius:50%;border:7px solid var(--rose);margin:0 auto}
.offer-name{margin-top:24px;font-size:13px;font-weight:600;color:var(--white);letter-spacing:.5px}
.offer-note{margin-top:6px;font-size:12px;color:#a8918c}

/* features */
.feature-box{background:var(--blush)}
.feature-photo{border-radius:0}
.feature-icon{position:absolute}
.feature-title{position:absolute;font-size:25px;font-weight:600;line-height:33px;color:var(--ink)}
.feature-copy{position:absolute;font-size:11.5px;line-height:19.5px;color:var(--text);width:380px}

/* products */
.products-band{left:0;top:2417px;width:1200px;height:682px;background:var(--blush)}
.product{position:absolute;top:2515px;width:186px;text-align:center}
.product-img{position:relative;height:193px;border:1px solid #eadedb}
.sale-tag{position:absolute;right:6px;top:6px;background:var(--rose);color:var(--white);font-size:9px;padding:2px 7px;letter-spacing:.5px}
.product-name{margin-top:19px;font-size:14px;color:var(--ink)}
.product-price{margin-top:4px;font-size:12px;color:var(--rose)}
.all-btn{left:528px;top:2791px;width:143px;height:34px;border:1px solid var(--ink);font-size:11px;letter-spacing:2px;color:var(--ink);display:flex;align-items:center;justify-content:center}
.video{left:273px;top:2918px;width:654px;height:317px;background:linear-gradient(120deg,#d9c2b6 0%,#b49385 45%,#8d6e62 100%)}
.play{left:570px;top:3046px;width:60px;height:60px;border-radius:50%;background:var(--white);display:flex;align-items:center;justify-content:center}

/* testimonials */
.avatar{left:561px;top:3333px;width:78px;height:78px;border-radius:50%;background:radial-gradient(circle at 50% 40%,#e9cfc3,#b9d2d8)}
.quote{left:0;top:3425px;width:1200px;text-align:center;font-size:12.5px;line-height:20px;color:var(--text)}
.quote-author{left:0;top:3478px;width:1200px;text-align:center;font-size:12px;font-weight:600;color:var(--ink)}
.slider-arrows{left:582px;top:3522px;display:flex;gap:12px}

/* map */
.map{left:0;top:3581px;width:1200px;height:348px;background:linear-gradient(135deg,#f3f2f1,#e9e8e7 50%,#f5f4f3)}
.store-card{left:199px;top:3663px;width:306px;height:184px;background:var(--white);box-shadow:0 4px 14px rgba(0,0,0,.12);text-align:center}
.store-card h3{margin-top:26px;font-size:21px;font-weight:600;color:var(--ink);letter-spacing:1px}
.store-card p{font-size:11.5px;line-height:18px;color:var(--ink)}

/* footer */
.footer{left:0;top:3929px;width:1200px;height:308px;background:var(--cocoa-deep);color:#e9dedc}
.footer-brand{left:199px;top:88px;color:var(--white)}
.footer-col{position:absolute;top:68px}
.footer-col h4{font-size:13px;font-weight:600;letter-spacing:1px;color:var(--white);margin-bottom:17px}
.footer-col li{list-style:none;font-size:11.5px;line-height:22.5px;color:#e9dedc}
.footer-col li.link::before{content:"›";margin-right:10px;color:#bca8a4}
.socials{display:flex;gap:12px;margin-top:10px}
.socials span{width:14px;height:14px;border-radius:50%;background:var(--rose)}
.copyright{left:0;top:262px;width:1200px;text-align:center;font-size:11px;color:#d8cac7}
</style>
</head>
<body>

<div class="abs promo-bar">Choose a beauty gift, FREE when you spend $99.00. See Details</div>

<section class="abs hero">
  <div class="abs brand header-brand"><span class="brand-dot"></span>Dewleaf Botanica</div>
  <nav class="abs main-nav">
    <span style="left:0">HOME</span>
    <span style="left:72px">ABOUT</span>
    <span style="left:151px">SKIN CARE</span>
    <span style="left:256px">BODY CARE</span>
    <span style="left:370px">OUR TREATMENTS</span>
    <span style="left:527px">CONTACT</span>
  </nav>
  <div class="abs nav-icons">
    <svg width="16" height="16" viewBox="0 0 16 16"><circle cx="6.5" cy="6.5" r="5" fill="none" stroke="#2f2a29" stroke-width="1.6"/><line x1="10.2" y1="10.2" x2="15" y2="15" stroke="#2f2a29" stroke-width="1.6"/></svg>
    <svg width="16" height="16" viewBox="0 0 16 16"><circle cx="8" cy="5" r="3.5" fill="none" stroke="#2f2a29" stroke-width="1.4"/><path d="M1.5 15c0-4 3-6 6.5-6s6.5 2 6.5 6" fill="none" stroke="#2f2a29" stroke-width="1.4"/></svg>
    <svg width="17" height="16" viewBox="0 0 17 16"><path d="M1 1.5h2.5l2 9h9l1.5-6.5H4.5" fill="none" stroke="#d0a29b" stroke-width="1.4"/><circle cx="6.5" cy="13.5" r="1.2" fill="#d0a29b"/><circle cx="13.5" cy="13.5" r="1.2" fill="#d0a29b"/></svg>
  </div>
  <h1 class="abs hero-title">Home Based<br>Organic Skin Care</h1>
  <p class="abs hero-sub">Bringing you a range of high-quality skin care made from 100% organic</p>
  <div class="abs signup"><span class="signup-field">Email Address</span><span class="signup-btn">Get Noticed</span></div>
  <div class="abs hero-photo" role="img" aria-label="Smiling woman touching her glowing cheek"></div>
</section>

<div class="abs about-photo" role="img" aria-label="Woman in a white robe applying skin care cream"></div>
<div class="abs about-inset" role="img" aria-label="Skin care bottle with botanicals"></div>
<h2 class="abs about-title">ABOUT US</h2>
<div class="abs about-copy">
  <p>Welcome to Dewleaf Botanica, Home based organic skin care manufacturer, bringing you a range of high-quality skin care made from 100% organic. Lorem ipsum dolor sit amet, consectetur adipiscing elit, sed do eiusmod tempor incididunt ut labore magn.</p>
  <p>Diam volutpat commodo sed egestas. Nisi quis eleifend quam adipiscing vitae proin sagittis nisl. Nulla malesuada pellentes elit eget gravida cum sociis natoque penatibus.</p>
</div>
<div class="btn" style="left:612px;top:939px;width:106px;height:33px">View More</div>

<section class="abs offers">
  <h2 class="section-title">What We Offers</h2>
  <div class="offer" style="left:327px"><div class="offer-circle" role="img" aria-label="Woman holding a jar of cream among green leaves" style="background:linear-gradient(135deg,#3f6b3a,#e6cfc4 55%,#f1e4dd)"></div><div class="offer-name">ORGANIC SOLUTION</div><div class="offer-note">Get the promo</div></div>
  <div class="offer" style="left:600px"><div class="offer-circle" role="img" aria-label="Client receiving a facial mask treatment" style="background:linear-gradient(135deg,#c7d3da,#f2ece9 50%,#d9c7be)"></div><div class="offer-name">TREATMENT</div><div class="offer-note">Start from $25.00</div></div>
  <div class="offer" style="left:873px"><div class="offer-circle" role="img" aria-label="Cream jars with cucumber slices and oil" style="background:linear-gradient(135deg,#f4f4f2,#e9ece4 50%,#b9c98d)"></div><div class="offer-name">EXCELLENT OFFERS</div><div class="offer-note">Get the promo</div></div>
</section>

<h2 class="section-title" style="top:1528px;line-height:28px">Connecting you with experts in<br>skin care and treatments</h2>

<div class="abs feature-box" style="left:316px;top:1647px;width:684px;height:359px"></div>
<div class="abs feature-photo" role="img" aria-label="Beautician applying a clay face mask with a brush" style="left:199px;top:1611px;width:370px;height:329px;background:linear-gradient(120deg,#e9dcd4,#a9b9a8 45%,#d7c3b7)"></div>
<svg class="feature-icon" style="left:616px;top:1686px" width="44" height="54" viewBox="0 0 44 54"><circle cx="22" cy="18" r="12" fill="none" stroke="#d0a29b" stroke-width="1.4"/><path d="M10 18c0-8 5-14 12-14s12 6 12 14c0 10 2 14 4 18M10 18c0 10-2 14-4 18M4 52c2-9 9-13 18-13s16 4 18 13" fill="none" stroke="#d0a29b" stroke-width="1.4"/></svg>
<h3 class="feature-title" style="left:610px;top:1756px">Only pay if your condition<br>improves after treatment</h3>
<p class="feature-copy" style="left:610px;top:1837px">Lorem ipsum dolor sit amet, consectetur adipiscing elit, sed do eiusmod tempor incididunt ut labore magn. Diam volutpat com sed egestas. Nisi quis eleifend quam adipiscing vitae proin sagittis nisl. Nulla malesuada pellentes elit eget.</p>
<div class="btn" style="left:610px;top:1932px;width:107px;height:33px">View More</div>

<div class="abs feature-box" style="left:610px;top:2104px;width:590px;height:313px"></div>
<div class="abs feature-photo" role="img" aria-label="Woman holding white baby's breath flowers over one eye" style="left:636px;top:2055px;width:364px;height:332px;background:linear-gradient(120deg,#dfe2e4,#e8d2c8 50%,#cfd6d9)"></div>
<svg class="feature-icon" style="left:199px;top:2108px" width="56" height="42" viewBox="0 0 56 42"><rect x="2" y="14" width="34" height="24" rx="4" fill="none" stroke="#d0a29b" stroke-width="1.4"/><path d="M2 22h34M12 14V8h14v6" fill="none" stroke="#d0a29b" stroke-width="1.4"/><ellipse cx="44" cy="24" rx="9" ry="14" fill="none" stroke="#d0a29b" stroke-width="1.4"/></svg>
<h3 class="feature-title" style="left:199px;top:2167px">Speak to a professional<br>without the in person</h3>
<p class="feature-copy" style="left:199px;top:2249px">Lorem ipsum dolor sit amet, consectetur adipiscing elit, sed do eiusmod tempor incididunt ut labore magn. Diam volutpat com sed egestas. Nisi quis eleifend quam adipiscing vitae proin sagittis nisl. Nulla malesuada pellentes elit eget.</p>
<div class="btn" style="left:199px;top:2346px;width:107px;height:33px">View More</div>

<div class="abs products-band"></div>
<h2 class="section-title" style="top:2463px">Top Selling Products</h2>
<div class="product" style="left:199px"><div class="product-img" role="img" aria-label="Age Reverse Serum product label" style="background:#f3ead7"><span class="sale-tag">SALE</span></div><div class="product-name">Age Reverse Serum</div><div class="product-price">£12.99</div></div>
<div class="product" style="left:404px"><div class="product-img" role="img" aria-label="Balancing Facial Toner product label" style="background:#fbfafa"><span class="sale-tag">SALE</span></div><div class="product-name">Balancing Facial Toner</div><div class="product-price">£12.99</div></div>
<div class="product" style="left:610px"><div class="product-img" role="img" aria-label="Brightening Body Milk product label" style="background:#f8f8f9"></div><div class="product-name">Brightening Body Milk</div><div class="product-price">£12.99</div></div>
<div class="product" style="left:814px"><div class="product-img" role="img" aria-label="Brightening Body Wash product label" style="background:#b39bcc"></div><div class="product-name">Brightening Body Wash</div><div class="product-price">£12.99</div></div>
<div class="abs all-btn">ALL PRODUCTS</div>

<h2 class="section-title" style="top:2872px">How It Works</h2>
<div class="abs video" role="img" aria-label="Video still of a woman in a towel applying face cream"></div>
<div class="abs play"><svg width="20" height="22" viewBox="0 0 20 22"><path d="M3 1l16 10L3 21z" fill="#4a3734"/></svg></div>

<h2 class="section-title" style="top:3284px">Testimonials</h2>
<div class="abs avatar" role="img" aria-label="Customer portrait"></div>
<p class="abs quote">Diam volutpat commodo sed egestas. Nisi quis eleifend quam adipiscing vitae proin sagittis<br>nisl. Nulla malesuada pellentes elit eget gravida cum sociis natoque et ut labore.</p>
<p class="abs quote-author">- Maren</p>
<div class="abs slider-arrows">
  <svg width="10" height="16" viewBox="0 0 10 16"><path d="M8 2L2 8l6 6" fill="none" stroke="#d0a29b" stroke-width="1.4"/></svg>
  <svg width="10" height="16" viewBox="0 0 10 16"><path d="M2 2l6 6-6 6" fill="none" stroke="#d0a29b" stroke-width="1.4"/></svg>
</div>

<div class="abs map" role="img" aria-label="Street map around the studio location"></div>
<div class="abs store-card">
  <h3>DEWLEAF BOTANICA</h3>
  <p style="margin-top:12px">14 Fern Row</p>
  <p>Hollin Lane LN4 2QX</p>
  <p>Mob: 020 5550 0142</p>
  <div class="btn" style="left:79px;top:125px;width:149px;height:33px">Get Direction</div>
</div>

<footer class="abs footer">
  <div class="abs brand footer-brand"><span class="brand-dot"></span>Dewleaf Botanica</div>
  <div class="footer-col" style="left:406px"><h4>TREATMENTS</h4><ul><li class="link">Skin Care</li><li class="link">Body Care</li><li class="link">Nails</li><li class="link">Appliances</li></ul></div>
  <div class="footer-col" style="left:610px"><h4>QUICK LINKS</h4><ul><li class="link">About us</li><li class="link">Contact us</li><li class="link">Blog</li><li class="link">FAQ</li><li class="link">Privacy Policy</li><li class="link">Terms and Conditions</li></ul></div>
  <div class="footer-col" style="left:835px"><h4>ADDRESS</h4><ul><li>14 Fern Row</li><li>Hollin Lane LN4 2QX</li><li>Mob: 020 5550 0142</li><li>E-mail: hello@dewleafbotanica.com</li></ul><div class="socials"><span></span><span></span><span></span></div></div>
  <p class="abs copyright">© Dewleaf Botanica 2023. All rights reserved.</p>
</footer>

</body>
</html>
```